Need a Sales Event Design/Logo with newspaper boilerplate. Big attention grabbing logo/type at the top with border around. Must be colorful, include artwork and be attention getting.

NAME:
Silver Pine Event
TAGLINE:
Do what car buyers recommend and get your best deal at year’s end.
CLIENT:
Brookvale Corvanta (This must be editable)
CREATIVE BRIEF:
This is a sales event for car dealership that is meant to grab eyeballs. The mental thought it should relay is that the end of the year is the very best time to buy and this is the event you should shop. You may want to tie in Alarms / Clocks / visually to help convey message.
GRAPHIC PRESENTATION:
Looking for Big Bold, Colorful attention grabbing sales event logo that can serve as a boilerplate to print or billboard advertisement. Must be able to customize with fonts embedded. Possibly 3D?
Sample attached:
FORMATS NEEDED:
Need in these formats for both CYMK & RGB: .ai *.eps * .pdf (editable) * .jpeg * .png * .psd
OWNERSHIP:
Once design has been paid for all rights to the design belong solely to purchaser in perpetuity.

Industry/Entity Type

Event

Requirements
Must have
• Must have eyepopping artwork and Event Name and Tagline.

```html
<!DOCTYPE html>
<html lang="en">
<head>
<meta charset="utf-8">
<title>Silver Pine Event – Newspaper Boilerplate</title>
<link href="https://fonts.googleapis.com/css2?family=PT+Sans+Narrow:wght@700&family=Quicksand:wght@500&display=swap" rel="stylesheet">
<style>
  :root {
    --event-red: #b21d2f;
    --event-red-dark: #7e1020;
    --frame-ink: #1e1e1e;
    --paper: #ffffff;
    --panel-light: #f6f6f7;
    --panel-grey: #dcdcde;
    --contact-ink: #3a3a3a;
  }
  html, body {
    margin: 0;
    padding: 0;
    width: 955px;
    height: 1200px;
    overflow: hidden;
    background: var(--paper);
  }
  .sheet {
    position: relative;
    width: 955px;
    height: 1200px;
  }
  .crop-marks {
    position: absolute;
    inset: 0;
  }
  .ad-frame {
    position: absolute;
    left: 76px;
    top: 82px;
    width: 809px;
    height: 1048px;
    border: 5px solid var(--frame-ink);
    border-radius: 40px;
    overflow: hidden;
    background: radial-gradient(ellipse at 50% 48%, var(--paper) 0%, var(--panel-light) 45%, var(--panel-grey) 100%);
  }
  .event-name {
    font-family: "PT Sans Narrow", "Arial Narrow", sans-serif;
    font-weight: 700;
    color: var(--event-red);
    margin: 0;
    line-height: 1;
    white-space: nowrap;
  }
  .event-mark {
    position: absolute;
    display: flex;
    align-items: center;
    gap: 22px;
  }
  .event-mark-dot {
    flex: none;
    border-radius: 50%;
    background: var(--event-red);
  }
  .event-mark--headline {
    left: 50px;
    top: 150px;
  }
  .event-mark--headline .event-mark-dot { width: 120px; height: 120px; }
  .event-mark--headline .event-name { font-size: 96px; }

  .event-mark--backdrop {
    left: 90px;
    top: 545px;
    gap: 18px;
    opacity: 0.07;
  }
  .event-mark--backdrop .event-mark-dot { width: 140px; height: 140px; }
  .event-mark--backdrop .event-name { font-size: 88px; }

  .tagline {
    position: absolute;
    left: 148px;
    top: 282px;
    width: 560px;
  }
  .tagline-ribbon {
    display: block;
    width: max-content;
    background: var(--event-red);
    color: var(--paper);
    font-family: "PT Sans Narrow", "Arial Narrow", sans-serif;
    font-weight: 700;
    font-size: 33px;
    line-height: 1;
    padding: 10px 12px 12px;
    transform: rotate(-3deg);
    box-shadow: 3px 4px 0 var(--event-red-dark);
  }
  .tagline-ribbon + .tagline-ribbon {
    margin: 2px 0 0 16px;
  }

  .dealer-footer {
    position: absolute;
    left: 0;
    right: 0;
    bottom: 20px;
    height: 168px;
    background: linear-gradient(180deg, rgba(255,255,255,0.6), rgba(255,255,255,0.85));
  }
  .event-mark--footer {
    left: 22px;
    top: 52px;
    gap: 12px;
  }
  .event-mark--footer .event-mark-dot { width: 62px; height: 62px; }
  .event-mark--footer .event-name { font-size: 46px; }

  .dealer-contact {
    position: absolute;
    left: 450px;
    top: 14px;
    font-family: "Quicksand", "Varela Round", sans-serif;
    font-weight: 500;
    font-style: normal;
    color: var(--contact-ink);
  }
  .dealer-name {
    margin: 0 0 4px;
    font-size: 30px;
    font-weight: 500;
  }
  .dealer-line {
    margin: 0;
    font-size: 17px;
    line-height: 23px;
  }
</style>
</head>
<body>
<div class="sheet">
  <svg class="crop-marks" width="955" height="1200" aria-hidden="true">
    <g stroke="#222" stroke-width="1">
      <line x1="62" y1="12" x2="62" y2="38"/>
      <line x1="12" y1="62" x2="38" y2="62"/>
      <line x1="912" y1="12" x2="912" y2="38"/>
      <line x1="936" y1="62" x2="962" y2="62"/>
      <line x1="62" y1="1186" x2="62" y2="1212"/>
      <line x1="12" y1="1162" x2="38" y2="1162"/>
      <line x1="912" y1="1186" x2="912" y2="1212"/>
      <line x1="936" y1="1162" x2="962" y2="1162"/>
    </g>
  </svg>

  <main class="ad-frame">
    <div class="event-mark event-mark--backdrop" aria-hidden="true">
      <span class="event-mark-dot"></span>
      <span class="event-name">Silver Pine Event</span>
    </div>

    <header class="event-mark event-mark--headline">
      <span class="event-mark-dot"></span>
      <h1 class="event-name">Silver Pine Event</h1>
    </header>

    <div class="tagline">
      <span class="tagline-ribbon">Do what car buying experts recommend</span>
      <span class="tagline-ribbon">And get your best deal at year’s end!</span>
    </div>

    <footer class="dealer-footer">
      <div class="event-mark event-mark--footer">
        <span class="event-mark-dot"></span>
        <span class="event-name">Silver Pine Event</span>
      </div>
      <address class="dealer-contact">
        <p class="dealer-name">Car Dealers Name</p>
        <p class="dealer-line">Phone</p>
        <p class="dealer-line">Web</p>
        <p class="dealer-line">Add</p>
      </address>
    </footer>
  </main>
</div>
</body>
</html>
```